" A VELMIRA é uma empresa de consultoria de Administraçao Contratual de Obras (destacadamente no segmento de infraestrutura e construçao pesada); Elaboraçao de pleitos/reivindicaçoes ("claim") para reequilíbrio econômico-financeiro de contratos de empreendimentos; Gerenciamento de Projetos; Gestao de Empreendimentos; Fiscalizaçao; Auditoria; Gestao Empresarial; Planejamento e Controle de Obras; Análise de Riscos de Empreendimentos; Orçamentos; Suporte para elaboraçao, análise e gestao de contratos. A sede da VELMIRA fica em Brasília/DF, entretanto a atuaçao ocorre em todo o Brasil conforme demanda dos clientes e localizaçao de suas obras. "

```html
<!DOCTYPE html>
<html lang="pt-BR">
<head>
<meta charset="utf-8">
<title>VELMIRA – Papel timbrado</title>
<link href="https://fonts.googleapis.com/css2?family=Open+Sans:wght@400;600;700;800&display=swap" rel="stylesheet">
<style>
  :root {
    --backdrop: #ececec;
    --paper: #ffffff;
    --navy: #1d3d5c;
    --teal: #1f5d7a;
    --sky: #3a8bb5;
    --body-text: #6a6a6a;
    --contact-text: #555555;
    --seal: #b9bec3;
    --signature-tone: #d9dde0;
  }
  * { margin: 0; padding: 0; box-sizing: border-box; }
  html, body {
    width: 1200px; height: 1200px; overflow: hidden;
    background: var(--backdrop);
    font-family: "Open Sans", Arial, sans-serif;
  }
  .letterhead {
    position: absolute; left: 233px; top: 46px;
    width: 734px; height: 1107px;
    background: var(--paper);
    box-shadow: 0 2px 8px rgba(0,0,0,.12);
    overflow: hidden;
  }
  .side-rule {
    position: absolute; left: 0; top: 0;
    width: 17px; height: 826px;
    background: var(--teal);
  }
  .brand {
    position: absolute; right: 30px; top: 120px;
    display: flex; align-items: center; gap: 10px;
  }
  .brand-square { width: 16px; height: 16px; background: var(--navy); }
  .brand-name {
    font-weight: 800; font-size: 30px; letter-spacing: 1px;
    color: var(--navy);
  }
  .web-band {
    position: absolute; right: 0; top: 170px;
    width: 284px; height: 24px;
    background: var(--sky);
    color: #fff; font-size: 13px; font-weight: 600; letter-spacing: 1.6px;
    line-height: 24px; text-align: right; padding-right: 22px;
  }
  .letter-body {
    position: absolute; left: 54px; width: 632px;
    font-size: 12.5px; line-height: 1.5; color: var(--body-text);
  }
  .p-one { top: 265px; }
  .p-two { top: 421px; }
  .p-three { top: 575px; }
  .signature {
    position: absolute; left: 478px; top: 764px;
    width: 108px; height: 62px;
    background: linear-gradient(100deg, var(--signature-tone), #eef0f1);
    border-radius: 30px;
  }
  .seal { position: absolute; left: 567px; top: 745px; }
  .contact-list { position: absolute; left: 27px; top: 845px; list-style: none; }
  .contact-item {
    display: flex; align-items: center; gap: 12px;
    height: 20px; margin-bottom: 21px;
    font-size: 13px; color: var(--contact-text);
  }
  .contact-icon {
    width: 18px; height: 18px; background: var(--sky);
    display: flex; align-items: center; justify-content: center;
  }
  .address {
    position: absolute; left: 0; width: 100%; top: 1040px;
    text-align: center; font-size: 13.5px; line-height: 1.35; color: var(--contact-text);
  }
  .address-title { font-weight: 700; color: var(--navy); }
  .foot-strip {
    position: absolute; left: 208px; bottom: 0;
    width: 338px; height: 8px; background: var(--sky);
  }
</style>
</head>
<body>
<main class="letterhead">
  <div class="side-rule"></div>

  <div class="brand">
    <span class="brand-square"></span>
    <span class="brand-name">VELMIRA</span>
  </div>
  <div class="web-band">www.velmira.com.br</div>

  <p class="letter-body p-one">Prezados senhores, encaminhamos a presente correspondência para apresentar nossa proposta de consultoria em administração contratual de obras de infraestrutura. Nossa equipe técnica acompanha o contrato desde a fase de planejamento até a entrega final, com controle de prazos, custos e riscos. Permanecemos à disposição para esclarecer qualquer dúvida e agendar uma reunião com a sua equipe.</p>

  <p class="letter-body p-two">O escopo inclui a elaboração de pleitos para reequilíbrio econômico-financeiro, a análise de riscos do empreendimento, a revisão de orçamentos e o suporte na gestão dos contratos. Os relatórios serão enviados mensalmente, com indicadores claros de desempenho e recomendações objetivas para cada etapa da obra.</p>

  <p class="letter-body p-three">Atuamos a partir de Brasília em todo o território nacional, conforme a demanda de cada cliente e a localização de suas obras. Nossa experiência em construção pesada garante uma fiscalização rigorosa, auditorias independentes e um planejamento realista. Agradecemos a atenção e aguardamos o seu retorno para darmos início aos trabalhos com a máxima brevidade possível, sempre com transparência e compromisso com resultados.</p>

  <div class="signature" role="img" aria-label="Assinatura manuscrita do responsável"></div>
  <svg class="seal" width="92" height="92" viewBox="0 0 92 92" aria-hidden="true">
    <circle cx="46" cy="46" r="44" fill="none" stroke="var(--seal)" stroke-width="2"/>
  </svg>

  <ul class="contact-list">
    <li class="contact-item">
      <span class="contact-icon">
        <svg width="12" height="12" viewBox="0 0 24 24"><path fill="#fff" d="M6.6 10.8a15 15 0 0 0 6.6 6.6l2.2-2.2a1 1 0 0 1 1-.25 11.4 11.4 0 0 0 3.6.57 1 1 0 0 1 1 1V20a1 1 0 0 1-1 1A17 17 0 0 1 3 4a1 1 0 0 1 1-1h3.5a1 1 0 0 1 1 1c0 1.25.2 2.45.57 3.57a1 1 0 0 1-.25 1z"/></svg>
      </span>
      (61) 3204.5587 | (61) 3204.5588
    </li>
    <li class="contact-item">
      <span class="contact-icon">
        <svg width="12" height="10" viewBox="0 0 24 18"><rect x="1" y="1" width="22" height="16" fill="none" stroke="#fff" stroke-width="2"/><path d="M1 1l11 9 11-9" fill="none" stroke="#fff" stroke-width="2"/></svg>
      </span>
      contato@velmira.com.br
    </li>
    <li class="contact-item">
      <span class="contact-icon"></span>
      /velmira
    </li>
    <li class="contact-item">
      <span class="contact-icon"></span>
      @velmira
    </li>
  </ul>

  <address class="address">
    <div class="address-title">Endereço:</div>
    <div>SHS Quadra 6, 410 | Asa Sul | Brasília/DF</div>
    <div>Cep. 70316-900</div>
  </address>

  <div class="foot-strip"></div>
</main>
</body>
</html>
```